Business card and e-mail signature template.

I need a business card- and e-mail signature template for a project (signature will be used with gmail). The logo is attached.

There the logo has a focus on the “Lumora” part of the name. The URL for the project is www.lumorafest.com.
The full name of the project is The Lumora Expo. The project will be publicly known as “Lumora” or “Lumora2020”. In all documents we will present the project as Lumora2020.

The logo can contain design elements and the design should be modern and appealing to both young people and traditional companies.

This competition is part of a bigger delivery. The winner will therefore be a strong candidate for the brand guide og maybe website.

```html
<!DOCTYPE html>
<html lang="en">
<head>
<meta charset="utf-8">
<title>Lumora2020 – Business Card</title>
<link rel="stylesheet" href="https://fonts.googleapis.com/css2?family=Lato:wght@400;700&display=swap">
<style>
  :root {
    --stage: #1c1c1d;
    --card: #0b0b0c;
    --white: #ffffff;
    --text: #e9e9e9;
    --pink: #ee1f5f;
    --orange: #f7941d;
    --teal: #13b5b1;
    --purple: #8e2a8c;
  }
  * { box-sizing: border-box; margin: 0; padding: 0; }
  html, body {
    width: 1200px; height: 1200px; overflow: hidden;
    background: var(--stage);
    font-family: "Lato", sans-serif;
  }
  .card {
    position: absolute;
    left: 217px;
    width: 763px;
    height: 435px;
    background: var(--card);
    box-shadow: 0 6px 18px rgba(0,0,0,.45);
  }
  .card--front { top: 149px; }
  .card--back { top: 608px; }

  .wordmark {
    position: absolute;
    display: flex;
    align-items: center;
    gap: 14px;
    transform: translate(-50%, -50%);
  }
  .wordmark__dot {
    width: 22px; height: 22px; border-radius: 50%;
    background: var(--pink);
  }
  .wordmark__name {
    font-weight: 700;
    font-size: 46px;
    letter-spacing: 1px;
    color: var(--white);
  }
  .card--front .wordmark { left: 383px; top: 218px; }
  .card--back .wordmark { left: 212px; top: 210px; }
  .card--back .wordmark__name { font-size: 40px; }

  .divider {
    position: absolute;
    left: 416px; top: 0;
    width: 30px; height: 100%;
  }
  .contact {
    position: absolute;
    left: 465px; top: 90px;
    color: var(--text);
  }
  .contact__name {
    font-size: 27px;
    line-height: 1;
  }
  .contact__first { color: var(--orange); font-weight: 700; }
  .contact__last { color: var(--teal); font-weight: 400; }
  .contact__role {
    margin-top: 14px;
    font-size: 18px;
  }
  .contact__address {
    margin-top: 26px;
    font-size: 17px;
    line-height: 25px;
  }
  .contact__list {
    list-style: none;
    margin-top: 18px;
  }
  .contact__item {
    display: flex;
    align-items: center;
    gap: 10px;
    height: 37px;
    font-size: 17px;
  }
  .icon {
    width: 25px; height: 25px; border-radius: 50%;
    display: flex; align-items: center; justify-content: center;
  }
  .icon--phone { background: var(--teal); }
  .icon--mail { background: var(--orange); }
  .icon--web { background: var(--pink); }
</style>
</head>
<body>
  <section class="card card--front">
    <div class="wordmark">
      <span class="wordmark__dot"></span>
      <span class="wordmark__name">Lumora2020</span>
    </div>
  </section>

  <section class="card card--back">
    <div class="wordmark">
      <span class="wordmark__dot"></span>
      <span class="wordmark__name">Lumora2020</span>
    </div>

    <svg class="divider" viewBox="0 0 30 435" aria-hidden="true">
      <line x1="15" y1="101" x2="15" y2="349" stroke="var(--orange)" stroke-width="2"/>
      <circle cx="15" cy="101" r="12" fill="var(--teal)"/>
      <circle cx="15" cy="349" r="12" fill="var(--teal)"/>
    </svg>

    <div class="contact">
      <p class="contact__name"><span class="contact__first">Daniel</span> <span class="contact__last">Reyes</span></p>
      <p class="contact__role">Financial Advisor</p>
      <p class="contact__address">4127 Harbor Lane,<br>Millbrook, NY 12545</p>
      <ul class="contact__list">
        <li class="contact__item">
          <span class="icon icon--phone">
            <svg width="14" height="14" viewBox="0 0 24 24"><path fill="#fff" d="M6.6 10.8a15.1 15.1 0 0 0 6.6 6.6l2.2-2.2c.3-.3.7-.4 1-.2 1.1.4 2.3.6 3.6.6.6 0 1 .4 1 1V20c0 .6-.4 1-1 1A17 17 0 0 1 3 4c0-.6.4-1 1-1h3.5c.6 0 1 .4 1 1 0 1.3.2 2.5.6 3.6.1.3 0 .7-.2 1z"/></svg>
          </span>
          <span>555-302-0147</span>
        </li>
        <li class="contact__item">
          <span class="icon icon--mail">
            <svg width="14" height="14" viewBox="0 0 24 24"><rect x="2" y="5" width="20" height="14" rx="1.5" fill="#fff"/><path d="M3 6l9 7 9-7" fill="none" stroke="var(--orange)" stroke-width="2"/></svg>
          </span>
          <span>daniel@lumorafest.com</span>
        </li>
        <li class="contact__item">
          <span class="icon icon--web">
            <svg width="15" height="15" viewBox="0 0 24 24" fill="none" stroke="#fff" stroke-width="2"><circle cx="12" cy="12" r="9"/><ellipse cx="12" cy="12" rx="4" ry="9"/><line x1="3" y1="12" x2="21" y2="12"/></svg>
          </span>
          <span>www.lumorafest.com</span>
        </li>
      </ul>
    </div>
  </section>
</body>
</html>
```